New business card design to go with our new logo

just want an eye-catching business card to go with our new logo. We are open to double sided or single sided. Just want it to have the following info on it. Whatever layout you think looks best.

First and Last Name
Title
Phone 801-555-7392
Address 214 W. Cedar Lane Pleasant Grove UT 84062
Email thecrew@marloweskennelandtreat.example

```html
<!DOCTYPE html>
<html lang="en">
<head>
<meta charset="utf-8">
<title>Marlowe's Kennel &amp; Treat — Business Card</title>
<link rel="stylesheet" href="https://fonts.googleapis.com/css2?family=Roboto:wght@400;700&display=swap">
<style>
  :root {
    --stage: #3d3d3f;
    --brand-blue: #38a6d6;
    --brand-orange: #f08a4b;
    --card-white: #ffffff;
    --ink: #3a3a3a;
    --muted: #6b6b6b;
  }
  * { box-sizing: border-box; margin: 0; padding: 0; }
  html, body {
    width: 1200px; height: 810px; overflow: hidden;
    background: var(--stage);
    font-family: "Roboto", Arial, sans-serif;
  }
  .stage {
    width: 1200px; height: 810px;
    display: flex; align-items: center; justify-content: center; gap: 40px;
  }
  .card {
    position: relative; width: 560px; height: 320px; overflow: hidden;
    box-shadow: 0 10px 24px rgba(0,0,0,.35);
  }
  /* Front */
  .card-front {
    background: var(--brand-blue);
    display: flex; align-items: center; justify-content: center;
  }
  .front-wordmark {
    text-align: center; color: var(--card-white); font-weight: 700;
    font-size: 44px; letter-spacing: 1px; line-height: 1.05;
  }
  .front-wordmark .tagline { display: block; font-size: 20px; letter-spacing: 3px; margin-top: 6px; }
  .front-rule { display: block; width: 240px; height: 2px; background: var(--card-white); margin: 12px auto 0; }
  /* Back */
  .card-back { background: var(--card-white); }
  .back-wordmark {
    position: absolute; top: 30px; right: 40px; width: 250px; text-align: center;
    color: var(--brand-orange); font-weight: 700; font-size: 28px; line-height: 1.1;
  }
  .back-wordmark .tagline { display: block; font-size: 13px; letter-spacing: 2px; margin-top: 2px; }
  .back-rule { position: absolute; top: 94px; right: 80px; width: 170px; height: 2px; background: var(--brand-blue); }
  .person { position: absolute; left: 44px; top: 150px; }
  .person-name { color: var(--brand-blue); font-weight: 700; font-size: 26px; }
  .person-title { color: var(--muted); font-size: 14px; margin-top: 4px; }
  .contact {
    position: absolute; left: 272px; top: 108px; width: 276px;
    font-size: 11.5px; color: var(--ink); line-height: 1.4;
  }
  .contact .address { margin-bottom: 4px; }
  .contact-row { display: flex; align-items: center; gap: 7px; white-space: nowrap; }
  .contact-row svg { width: 11px; height: 11px; flex: none; }
  .contact .web-domain { color: var(--brand-blue); }
  .swoosh { position: absolute; left: 0; bottom: 0; width: 560px; height: 110px; }
</style>
</head>
<body>
<main class="stage">
  <section class="card card-front" aria-label="Card front">
    <div class="front-wordmark">
      MARLOWE'S
      <span class="tagline">KENNEL &amp; TREAT</span>
      <span class="front-rule"></span>
    </div>
  </section>

  <section class="card card-back" aria-label="Card back">
    <div class="back-wordmark">MARLOWE'S<span class="tagline">KENNEL &amp; TREAT</span></div>
    <span class="back-rule"></span>

    <div class="person">
      <p class="person-name">Dana Whitfield</p>
      <p class="person-title">CEO &amp; President</p>
    </div>

    <div class="contact">
      <p class="address">214 W. Cedar Lane<br>Pleasant Grove UT 84062</p>
      <p class="contact-row">
        <svg viewBox="0 0 12 12"><path d="M3 1 L5 3.5 L4 5 Q5 7 7 8 L8.5 7 L11 9 L9.5 11 Q5 11 2.5 7.5 Q1 5 1.5 2.5 Z" fill="var(--brand-blue)"/></svg>
        801-555-7392
      </p>
      <p class="contact-row">
        <svg viewBox="0 0 12 12"><rect x="0.5" y="2.5" width="11" height="7" fill="var(--brand-blue)"/><path d="M0.5 2.5 L6 6.5 L11.5 2.5" stroke="#fff" fill="none"/></svg>
        thecrew@marloweskennelandtreat.example
      </p>
      <p class="contact-row">
        <svg viewBox="0 0 12 12" fill="none" stroke="var(--brand-blue)" stroke-width="1.1"><circle cx="6" cy="6" r="5"/><ellipse cx="6" cy="6" rx="2.2" ry="5"/><path d="M1 6 H11"/></svg>
        <span>www.<span class="web-domain">marloweskennelandtreat.example</span></span>
      </p>
    </div>

    <svg class="swoosh" viewBox="0 0 560 110" preserveAspectRatio="none" aria-hidden="true">
      <path d="M0 110 L0 84 Q300 76 560 22 L560 110 Z" fill="var(--brand-blue)"/>
      <path d="M70 78 Q330 62 560 8 L560 15 Q330 70 70 78 Z" fill="var(--brand-orange)"/>
    </svg>
  </section>
</main>
</body>
</html>
```